Legal Agribusiness Capability Brochure Design

Design A4 sized 6 page Legal Agribusiness Capability Brochure. Design is to be consistent with current marketing materials - logo, letterhead, website and business card to be provided.
Cover page - Firm name and logo, Agribusiness Capability Statement heading with image 1 below
Inside cover page - About Us section with image 2 below then Awards section below image
Inside middle page - Our Expertise with image 3 below
Inside back page - Our Experience with image 4 below
Back page - Senior Lawyers with image 5 below
Outside Middle Back Page - Contact Us with image 6
Updates

To provide more details to designers for brochure

Target Market(s)

Agribusiness - Australia

Industry/Entity Type

Legal

Colors

Designer to choose colors to be used in the design.

Requirements
Must have
• Use content from uloaded file - Agribusiness Brochure Content
• Use images uploaded
• Professional appearance
• Consistent with current marketing and website https://tallowcreeklegal.com.au/

```html
<!DOCTYPE html>
<html lang="en">
<head>
<meta charset="utf-8">
<title>Tallow Creek Legal – Agribusiness Capability Spread</title>
<link href="https://fonts.googleapis.com/css2?family=Lora:ital,wght@0,400;1,400&family=Raleway:wght@400;500;600&display=swap" rel="stylesheet">
<style>
  :root {
    --backdrop: #e6e6e6;
    --sky-blue: #2f6fb8;
    --deep-blue: #0d4fa3;
    --pale-sky: #a9c9e0;
    --wheat-gold: #c9923f;
    --wheat-light: #e2c089;
    --field-green: #1f7a3a;
    --dark-green: #0f4a26;
    --white: #ffffff;
    --brand-blue: #2a8ad4;
    --dot-gold: #e2a23a;
    --dot-teal: #2aa3a0;
    --dot-red: #d9533f;
  }
  * { box-sizing: border-box; margin: 0; padding: 0; }
  html, body { width: 1200px; height: 825px; overflow: hidden; background: var(--backdrop); }
  .spread {
    position: absolute; left: 80px; top: 45px;
    width: 1040px; height: 735px; display: flex;
    box-shadow: 0 10px 30px rgba(0,0,0,0.25);
  }
  .page { position: relative; width: 520px; height: 735px; overflow: hidden; }
  .page-photo { position: absolute; inset: 0; }

  .page--award .page-photo {
    background: linear-gradient(170deg, var(--pale-sky) 0%, #8fb3cf 28%, var(--wheat-light) 58%, var(--wheat-gold) 100%);
  }
  .award-statement {
    position: absolute; left: 56px; top: 250px; width: 420px;
    font-family: "Lora", serif; font-style: italic; color: var(--white);
    font-size: 34px; line-height: 1.2;
    text-shadow: 0 1px 4px rgba(0,0,0,0.2);
  }
  .award-statement .award-source { display: block; font-size: 24px; margin-top: 4px; }
  .firm-name {
    position: absolute; left: 0; right: 0; bottom: 70px;
    display: flex; align-items: center; justify-content: center; gap: 10px;
    font-family: "Raleway", sans-serif; font-weight: 600; font-size: 20px;
    color: var(--white); letter-spacing: 0.06em; text-transform: uppercase;
  }
  .firm-name .firm-mark { width: 16px; height: 16px; background: var(--brand-blue); }

  .page--experience .page-photo {
    background: linear-gradient(180deg, var(--deep-blue) 0%, var(--sky-blue) 22%, #1f6a6a 45%, var(--field-green) 70%, var(--dark-green) 100%);
  }
  .experience-heading {
    position: absolute; right: 50px; top: 60px;
    font-family: "Lora", serif; font-weight: 400; font-size: 36px; color: var(--white);
  }
  .experience-intro {
    position: absolute; left: 50px; top: 130px; width: 420px;
    font-family: "Raleway", sans-serif; font-size: 11.5px; line-height: 1.45; color: var(--white);
  }
  .industry-list {
    position: absolute; left: 70px; top: 320px; width: 400px;
    display: grid; grid-template-columns: 1fr 1fr; grid-auto-flow: column;
    grid-template-rows: repeat(6, 48px); column-gap: 30px;
    list-style: none;
    font-family: "Raleway", sans-serif; font-size: 16px; color: var(--white);
  }
  .industry-list li { display: flex; align-items: center; gap: 12px; }
  .industry-dot { width: 26px; height: 26px; border-radius: 50%; flex: none; }
  .dot-gold { background: var(--dot-gold); }
  .dot-teal { background: var(--dot-teal); }
  .dot-red { background: var(--dot-red); }
  .page-fold {
    position: absolute; left: 0; top: 0; bottom: 0; width: 24px;
    background: linear-gradient(90deg, rgba(0,0,0,0.25), rgba(0,0,0,0));
  }
</style>
</head>
<body>
  <main class="spread">
    <section class="page page--award">
      <div class="page-photo" role="img" aria-label="Close-up photograph of golden wheat ears against a soft blue sky"></div>
      <h2 class="award-statement">Ranked as a leading agribusiness law firm in Western Australia <span class="award-source">by Harrow’s Guide</span></h2>
      <div class="firm-name"><span class="firm-mark"></span>Tallow Creek Legal</div>
    </section>
    <section class="page page--experience">
      <div class="page-photo" role="img" aria-label="Photograph of green wheat stalks in a field under a blue sky"></div>
      <div class="page-fold"></div>
      <h2 class="experience-heading">Our Experience</h2>
      <p class="experience-intro">Our senior lawyers have over 60 years combined experience in advising a diverse range of clients such as governments and government bodies, listed public companies, private companies, accounting practices, insurance and financial service firms, agribusiness operators, horticulture operators, fishing operators, property developers and investors, real estate agents and settlement agents, mining companies and investors, hospital operators, SME’s, sole traders and high net individual clients on commercial and litigation issues relating to the following industries:</p>
      <ul class="industry-list">
        <li><span class="industry-dot dot-gold"></span>agriculture</li>
        <li><span class="industry-dot dot-gold"></span>fisheries</li>
        <li><span class="industry-dot dot-red"></span>manufacturing</li>
        <li><span class="industry-dot dot-teal"></span>transport</li>
        <li><span class="industry-dot dot-red"></span>property</li>
        <li><span class="industry-dot dot-gold"></span>construction</li>
        <li><span class="industry-dot dot-teal"></span>forestry</li>
        <li><span class="industry-dot dot-gold"></span>mining</li>
        <li><span class="industry-dot dot-teal"></span>hospitality</li>
        <li><span class="industry-dot dot-teal"></span>tourism</li>
        <li><span class="industry-dot dot-red"></span>franchising</li>
        <li><span class="industry-dot dot-red"></span>service industries</li>
      </ul>
    </section>
  </main>
</body>
</html>
```